Consulting company needs Business Cards - rough concept provided

I'm looking for someone to take our business card idea and make is slick and polished - to communicate our high-end, sophisticated, serious consulting business. We have a rough layout we did in-house. We are open to ideas on repo-ing elements, adjusting sizes, typefaces etc... within the general concept we've already come up with. We want it to be super-clean and sophisticated. We want to keep the white backgrounds, and blue brand colors. Our goal is to print with painted blue edges on thick cardstock. Thank you!!

```html
<!DOCTYPE html>
<html lang="en">
<head>
<meta charset="utf-8">
<title>Tallcrest Business Card</title>
<link rel="stylesheet" href="https://fonts.googleapis.com/css2?family=Italiana&family=Poppins:wght@300;400;600;800&display=swap">
<style>
  :root {
    --backdrop: #9eacba;
    --card: #ffffff;
    --brand-blue: #0a9cdc;
    --light-blue: #6cc6ee;
    --ink: #1b1b1b;
    --muted: #b4b7bb;
    --rule: #c9c9c9;
  }
  * { margin: 0; padding: 0; box-sizing: border-box; }
  html, body { width: 750px; height: 1200px; overflow: hidden; }
  body {
    background: var(--backdrop);
    font-family: "Poppins", sans-serif;
    position: relative;
  }
  .card {
    position: absolute;
    left: 75px;
    width: 600px;
    height: 334px;
    background: var(--card);
    box-shadow: 0 4px 10px rgba(40, 55, 70, 0.18);
    overflow: hidden;
  }
  .card--front { top: 250px; }
  .card--back { top: 616px; }

  .wordmark {
    position: absolute;
    top: 0;
    left: 0;
    width: 600px;
    height: 60px;
    display: block;
    overflow: hidden;
  }
  .wordmark__text {
    font-family: "Poppins", sans-serif;
    font-weight: 800;
    font-size: 86px;
    fill: var(--brand-blue);
  }

  .identity { position: absolute; left: 65px; top: 160px; }
  .identity__name {
    font-family: "Italiana", serif;
    font-size: 29px;
    color: var(--ink);
    line-height: 1.1;
  }
  .identity__role {
    display: flex;
    align-items: flex-end;
    font-size: 14px;
    font-weight: 400;
    color: var(--ink);
    letter-spacing: 0.4px;
    line-height: 1.2;
  }
  .identity__rule {
    width: 49px;
    height: 1px;
    background: var(--brand-blue);
    margin: 0 0 3px 4px;
  }

  .contact {
    position: absolute;
    right: 48px;
    top: 227px;
    text-align: right;
    font-size: 13.5px;
    color: var(--ink);
    line-height: 16px;
  }
  .contact__row { display: flex; justify-content: flex-end; align-items: center; gap: 8px; }
  .contact__row--plain { padding-right: 17px; }
  .contact__divider {
    height: 1px;
    width: 168px;
    margin: 6px 0 5px auto;
    background: var(--rule);
  }
  .contact__icon { width: 9px; height: 9px; flex: none; }

  .mission {
    position: absolute;
    left: 0;
    top: 104px;
    width: 600px;
    text-align: center;
    font-size: 23px;
    line-height: 42px;
    font-weight: 300;
    color: var(--muted);
  }
  .mission__key { font-weight: 600; color: var(--brand-blue); }

  .dots {
    position: absolute;
    top: 271px;
    left: 0;
    width: 600px;
    display: flex;
    justify-content: center;
    align-items: center;
    gap: 7px;
  }
  .dot { border-radius: 50%; }
  .dot--light { width: 8px; height: 8px; background: var(--light-blue); }
  .dot--main { width: 10px; height: 10px; background: var(--brand-blue); }
  .dot--grey { width: 8px; height: 8px; background: var(--muted); }
</style>
</head>
<body>
  <section class="card card--front" aria-label="Business card front">
    <svg class="wordmark" viewBox="0 0 600 60" aria-label="TALLCREST">
      <text class="wordmark__text" x="0" y="56" textLength="600" lengthAdjust="spacingAndGlyphs">TALLCREST</text>
    </svg>

    <div class="identity">
      <p class="identity__name">Dana Whitlow</p>
      <p class="identity__role">Brand Consultant <span class="identity__rule"></span></p>
    </div>

    <div class="contact">
      <div class="contact__row">4580 Harbor Lane, Ste 210
        <svg class="contact__icon" viewBox="0 0 10 10" aria-hidden="true"><circle cx="5" cy="5" r="5" fill="#0a9cdc"/><path d="M5 2.2a1.9 1.9 0 0 0-1.9 1.9C3.1 5.5 5 7.8 5 7.8s1.9-2.3 1.9-3.7A1.9 1.9 0 0 0 5 2.2z" fill="#fff"/><circle cx="5" cy="4.1" r="0.7" fill="#0a9cdc"/></svg>
      </div>
      <div class="contact__row contact__row--plain">Fairmont, CA 90000</div>
      <div class="contact__divider"></div>
      <div class="contact__row">(555) 014 2290
        <svg class="contact__icon" viewBox="0 0 10 10" aria-hidden="true"><circle cx="5" cy="5" r="5" fill="#0a9cdc"/><path d="M3.3 2.6l1 1-.5.7a3.5 3.5 0 0 0 1.9 1.9l.7-.5 1 1-.6.8C4.9 7.3 2.7 5.1 2.5 3.2z" fill="#fff"/></svg>
      </div>
      <div class="contact__row">dana@tallcrest.com
        <svg class="contact__icon" viewBox="0 0 10 10" aria-hidden="true"><circle cx="5" cy="5" r="5" fill="#0a9cdc"/><circle cx="5" cy="5" r="2.6" fill="none" stroke="#fff" stroke-width="0.7"/><path d="M2.4 5h5.2M5 2.4c-1.3 1.5-1.3 3.7 0 5.2M5 2.4c1.3 1.5 1.3 3.7 0 5.2" fill="none" stroke="#fff" stroke-width="0.6"/></svg>
      </div>
    </div>
  </section>

  <section class="card card--back" aria-label="Business card back">
    <p class="mission">
      <span class="mission__key">We help</span> [target demographic] <span class="mission__key">achieve</span><br>
      [desired emotional outcome] <span class="mission__key">by</span> [our unique<br>
      approach] <span class="mission__key">because</span> [our brand beliefs]
    </p>
    <div class="dots" aria-hidden="true">
      <span class="dot dot--light"></span>
      <span class="dot dot--main"></span>
      <span class="dot dot--grey"></span>
    </div>
  </section>
</body>
</html>
```